Business Card Design Project

Hello- I am an interior stylist/product designer whose work is detail driven, very clean and transitional in style and I want my business card to reflect those qualities. I have a logo that I use on my website- my name and a hand drawn chandelier that I want incorporated into the design. However, "Design for the Home" needs to be changed to "Designs". I will be using cream colored stock and am thinking of gray text and logo. I need your help in pulling my card together since it will be the most used element and drive the design of the rest of my stationary suite.
Updates

Please note that I have changed my QR code from my cell # to my website. The new code will be downloaded now.

Reason: I want to thank everyone who has submitted designs- there are truly some very inspiring designs and I am very pleased. I want to make certain that I get this right and have an attractive and highly effective marketing tool when we are finished. With that said, I have run into a technical problem with one aspect of the card- a qr code for my website that was not part of the original brief. I will get that corrected today and post. Once I get that taken care of, I will post comments to all designs received do far. Thanks again for everyone's efforts, Risa

QR Code for the website is now uploaded. Thanks for your patience!

Target Market(s)

Upper middle class- mostly women

Industry/Entity Type

Business

Requirements
Must have
• Marisa Vantry Designs
"...to the last detail."
214-555-0148
marisavantry@plumwick.net
www.marisavantrydesigns-example.com
27083 Birchmont Court
Dallas, TX 75000
Nice to have
• Risa Vantry
Owner

```html
<!DOCTYPE html>
<html lang="en">
<head>
<meta charset="utf-8">
<title>Marisa Vantry Designs — Business Card</title>
<link rel="stylesheet" href="https://fonts.googleapis.com/css2?family=Titillium+Web:wght@300;400&display=swap">
<style>
  :root {
    --page: #efebe4;
    --stock: #e9dcbf;
    --stock-light: #efe5cd;
    --stock-dark: #dfcfad;
    --ink-gray: #4a4846;
    --print-white: #ffffff;
    --print-soft: rgba(255, 255, 255, 0.7);
  }
  * { margin: 0; padding: 0; box-sizing: border-box; }
  html, body {
    width: 1200px; height: 800px; overflow: hidden;
    background: var(--page);
    font-family: "Titillium Web", sans-serif;
  }
  .canvas {
    position: relative; width: 1200px; height: 800px;
    display: flex; align-items: center; justify-content: center; gap: 40px;
  }
  .card {
    position: relative; width: 540px; height: 309px; overflow: hidden;
    background:
      radial-gradient(ellipse 60% 50% at 30% 30%, var(--stock-light), transparent 70%),
      radial-gradient(ellipse 50% 60% at 75% 70%, var(--stock-dark), transparent 70%),
      var(--stock);
    box-shadow: 0 6px 18px rgba(0, 0, 0, 0.12);
  }
  .card-bands { position: absolute; inset: 0; width: 100%; height: 100%; }

  /* Front */
  .brand-lockup {
    position: absolute; left: 0; right: 0; top: 118px;
    display: flex; align-items: center; justify-content: center; gap: 10px;
  }
  .brand-dot { width: 8px; height: 8px; border-radius: 50%; background: var(--ink-gray); }
  .brand-name { font-size: 24px; font-weight: 400; color: var(--ink-gray); letter-spacing: 0.5px; }

  /* Back */
  .back-company {
    position: absolute; left: 20px; width: 262px; top: 98px;
    text-align: right; font-size: 21px; font-weight: 300; color: var(--print-white);
  }
  .back-divider {
    position: absolute; left: 296px; top: 76px; width: 1px; height: 92px;
    background: var(--print-white);
  }
  .owner-block { position: absolute; left: 314px; top: 72px; color: var(--print-white); }
  .owner-name { font-size: 18px; font-weight: 400; text-transform: uppercase; line-height: 1.1; }
  .owner-title { font-size: 15px; font-weight: 300; text-transform: uppercase; color: var(--print-soft); line-height: 1.1; }
  .contact-line {
    display: flex; align-items: center; gap: 10px;
    font-size: 13px; font-weight: 300; margin-top: 10px;
  }
  .contact-line svg { width: 14px; height: 14px; flex: none; }
  .contact-line .email { text-transform: uppercase; font-size: 11px; }
  .address-block {
    position: absolute; left: 188px; top: 196px;
    color: var(--print-white); font-size: 10.5px; font-weight: 300;
    text-transform: uppercase; line-height: 1.45;
  }
  .address-block .indent { padding-left: 22px; }
</style>
</head>
<body>
<main class="canvas">

  <section class="card card-front" aria-label="Card front">
    <svg class="card-bands" viewBox="0 0 540 309" aria-hidden="true">
      <defs>
        <linearGradient id="band-front" x1="0" y1="0" x2="1" y2="1">
          <stop offset="0" stop-color="#fff" stop-opacity="0.85"/>
          <stop offset="1" stop-color="#fff" stop-opacity="0.35"/>
        </linearGradient>
      </defs>
      <polygon points="0,205 0,255 95,309 180,309" fill="url(#band-front)"/>
      <polygon points="120,205 200,205 370,309 290,309" fill="url(#band-front)" opacity="0.6"/>
    </svg>
    <div class="brand-lockup">
      <span class="brand-dot"></span>
      <span class="brand-name">Marisa Vantry Designs</span>
    </div>
  </section>

  <section class="card card-back" aria-label="Card back">
    <svg class="card-bands" viewBox="0 0 540 309" aria-hidden="true">
      <defs>
        <linearGradient id="band-back" x1="0" y1="0" x2="1" y2="1">
          <stop offset="0" stop-color="#fff" stop-opacity="0.85"/>
          <stop offset="1" stop-color="#fff" stop-opacity="0.3"/>
        </linearGradient>
      </defs>
      <polygon points="0,150 0,200 150,309 225,309" fill="url(#band-back)"/>
      <polygon points="70,150 140,150 330,309 255,309" fill="url(#band-back)" opacity="0.55"/>
    </svg>

    <h1 class="back-company">Marisa Vantry Designs</h1>
    <div class="back-divider"></div>

    <div class="owner-block">
      <p class="owner-name">Risa Vantry</p>
      <p class="owner-title">Owner</p>
      <p class="contact-line">
        <svg viewBox="0 0 24 24" aria-hidden="true"><path fill="#fff" d="M6.6 10.8a15 15 0 0 0 6.6 6.6l2.2-2.2a1 1 0 0 1 1-.25 11.4 11.4 0 0 0 3.6.57 1 1 0 0 1 1 1V20a1 1 0 0 1-1 1A17 17 0 0 1 3 4a1 1 0 0 1 1-1h3.5a1 1 0 0 1 1 1c0 1.25.2 2.45.57 3.57a1 1 0 0 1-.25 1z"/></svg>
        <span>214-555-0148</span>
      </p>
      <p class="contact-line">
        <svg viewBox="0 0 24 24" aria-hidden="true"><path fill="#fff" d="M3 5h18v14H3z M3 5l9 7 9-7" stroke="#e9dcbf" stroke-width="1.5"/></svg>
        <span class="email">marisavantry@plumwick.net</span>
      </p>
    </div>

    <address class="address-block">
      <p>www.marisavantrydesigns-example.com</p>
      <p class="indent">27083 Birchmont Court</p>
      <p class="indent">Dallas, TX 75000</p>
    </address>
  </section>

</main>
</body>
</html>
```